Brisk Ledger Hub's Facebook Cover Design

I am in need of a social media cover for my company's Facebook account. Please leverage the green logos and color palette attached.

Brisk Ledger Hub offers 2 primary services:
1.) Business Automation Services
2.) AI (artificial intelligence integrations)

While a lot of what we do is highly technical, what we deliver is not. In a nutshell, we help our clients to connect their data regardless of what application that data is sitting in. Because we can connect that data, often times we can:

A.) offer more intelligent marketing and help our client increase their revenue.
B.) automate highly repetitive tasks using technology and drive down their costs thus saving them money
C.) help our clients use AI to better serve their customers

You can read a little bit about our company here: https://www.briskledgerhub.example

Our tagline is: "Connect data to increase the flow of profitability."

Visually, we'd like your help to illustrate the "connecting" of these applications. Please let me know if you have any questions.

Target Market(s)

Business Owners or Marketing Managers

Industry/Entity Type

Marketing technologies.

Font styles to use
Sans Serif

Requirements
Must have
• Please make every effort to have the cover compatible with the color palette of the attached images.
Should not have
• Please do not use the standard clipart or stock libraries of AI = robot. If you do, please make them small. We help business glue their data from different sources to solve real work problems. Little robots are overused.

```html
<!DOCTYPE html>
<html lang="en">
<head>
<meta charset="utf-8">
<title>Brisk Ledger Hub – Facebook Cover Concepts</title>
<link rel="stylesheet" href="https://fonts.googleapis.com/css2?family=Poppins:ital,wght@0,400;0,500;0,600;0,700;1,400&display=swap">
<style>
  :root{
    --green:#8fe33d;
    --ink:#4a5156;
    --line:#a3a8ab;
    --page:#ffffff;
    --card:#ffffff;
    --photo-deep:#0d3a4a;
    --photo-mid:#2a8ea3;
    --photo-light:#7fd3e0;
  }
  *{margin:0;padding:0;box-sizing:border-box}
  html,body{width:1200px;height:1027px;overflow:hidden;background:var(--page)}
  body{position:relative;font-family:"Poppins",sans-serif}
  .cover{position:absolute;left:94px;width:996px;height:369px;background:var(--card);
    box-shadow:0 10px 28px rgba(0,0,0,.22);overflow:hidden}
  .cover--angled{top:100px}
  .cover--rounded{top:545px}
  .cover svg{display:block;width:100%;height:100%}
  .tagline{font-family:"Poppins",sans-serif;font-size:22px;fill:var(--ink)}
  .tagline .accent{font-weight:700;fill:var(--green)}
  .tagline .soft{font-style:italic}
  .brand-name{font-family:"Poppins",sans-serif;font-weight:700;fill:var(--ink)}
  .brand-name--angled{font-size:21px}
  .brand-name--rounded{font-size:27px}
  .service{font-family:"Poppins",sans-serif;font-size:13px;fill:var(--ink)}
  .services-title{font-family:"Poppins",sans-serif;font-weight:600;font-size:15.5px}
</style>
</head>
<body>

<section class="cover cover--angled" aria-label="Cover concept with angled tiles">
  <svg viewBox="0 0 850 315" xmlns="http://www.w3.org/2000/svg">
    <defs>
      <linearGradient id="photoTone" x1="0" y1="0" x2="1" y2="1">
        <stop offset="0" stop-color="var(--photo-light)"/>
        <stop offset=".5" stop-color="var(--photo-mid)"/>
        <stop offset="1" stop-color="var(--photo-deep)"/>
      </linearGradient>
      <radialGradient id="flowGlow">
        <stop offset="0" stop-color="var(--green)" stop-opacity=".55"/>
        <stop offset="1" stop-color="var(--green)" stop-opacity="0"/>
      </radialGradient>
    </defs>

    <!-- corner accents -->
    <g class="corner-accents">
      <polygon points="0,0 20,0 48,28 0,58" fill="var(--green)"/>
      <polygon points="25,0 60,0 97,37 70,47" fill="none" stroke="var(--line)" stroke-width="1.5"/>
      <line x1="0" y1="222" x2="95" y2="315" stroke="var(--line)" stroke-width="1.5"/>
      <polygon points="0,282 35,315 0,315" fill="var(--green)"/>
    </g>

    <!-- tagline -->
    <text class="tagline" x="98" y="65"><tspan class="accent">Connect data</tspan><tspan class="soft"> to</tspan></text>
    <text class="tagline" x="98" y="100"><tspan class="soft">increase</tspan> the flow of</text>
    <text class="tagline" x="98" y="135">profitability.</text>

    <!-- brand name -->
    <text class="brand-name brand-name--angled" x="338" y="85">Brisk Ledger Hub</text>

    <!-- flow decoration area -->
    <ellipse cx="410" cy="180" rx="55" ry="65" fill="url(#flowGlow)" role="img" aria-label="Decorative green data-flow motif"/>

    <!-- services band -->
    <polygon points="0,175 268,175 290,197 268,219 0,219" fill="var(--green)"/>
    <polygon points="274,175 289,175 311,197 289,219 274,219 296,197" fill="var(--green)"/>
    <polygon points="292,175 307,175 329,197 307,219 292,219 314,197" fill="var(--green)"/>
    <text class="services-title" x="102" y="203" fill="#ffffff">2 primary services</text>

    <circle cx="111" cy="244" r="4" fill="none" stroke="var(--ink)" stroke-width="1.6"/>
    <text class="service" x="124" y="249">Business Automation Services</text>
    <circle cx="111" cy="271" r="4" fill="none" stroke="var(--ink)" stroke-width="1.6"/>
    <text class="service" x="124" y="276">AI (artificial intelligence integrations)</text>

    <!-- right side bands -->
    <g class="bands">
      <polygon points="470,0 495,0 575,80 560,90" fill="none" stroke="var(--line)" stroke-width="1.5"/>
      <polygon points="535,0 570,0 612,42 595,55" fill="var(--green)"/>
      <polygon points="678,0 740,0 712,28" fill="var(--green)"/>
      <polygon points="660,125 688,125 850,290 850,315 830,315" fill="none" stroke="var(--line)" stroke-width="1.5"/>
      <polygon points="632,165 655,145 815,315 772,315" fill="var(--green)"/>
    </g>

    <!-- photo tiles -->
    <g role="img" aria-label="Photo tiles: connected data network, AI dashboards, hand touching a growth chart, digital circuitry and glowing data screens">
      <polygon points="565,80 630,145 565,210 500,145" fill="url(#photoTone)"/>
      <polygon points="650,14 698,62 650,110 602,62" fill="url(#photoTone)"/>
      <polygon points="770,25 858,113 770,201 682,113" fill="url(#photoTone)"/>
      <polygon points="537,168 584,215 537,262 490,215" fill="url(#photoTone)"/>
      <polygon points="620,190 680,250 620,310 560,250" fill="url(#photoTone)"/>
    </g>
  </svg>
</section>

<section class="cover cover--rounded" aria-label="Cover concept with rounded frame">
  <svg viewBox="0 0 850 315" xmlns="http://www.w3.org/2000/svg">
    <defs>
      <linearGradient id="photoToneB" x1="0" y1="0" x2="1" y2="1">
        <stop offset="0" stop-color="var(--photo-mid)"/>
        <stop offset=".6" stop-color="var(--photo-deep)"/>
        <stop offset="1" stop-color="#0a1f2a"/>
      </linearGradient>
      <radialGradient id="flowGlowB">
        <stop offset="0" stop-color="var(--green)" stop-opacity=".55"/>
        <stop offset="1" stop-color="var(--green)" stop-opacity="0"/>
      </radialGradient>
    </defs>

    <!-- flow decoration areas -->
    <ellipse cx="800" cy="110" rx="95" ry="120" fill="url(#flowGlowB)" role="img" aria-label="Decorative green data-flow motif"/>
    <ellipse cx="10" cy="240" rx="55" ry="80" fill="url(#flowGlowB)" role="img" aria-label="Decorative green data-flow motif"/>
    <ellipse cx="215" cy="190" rx="90" ry="95" fill="url(#flowGlowB)" role="img" aria-label="Decorative green data-flow motif"/>

    <!-- brand name -->
    <text class="brand-name brand-name--rounded" x="239" y="88" text-anchor="middle">Brisk Ledger Hub</text>

    <!-- photo circle -->
    <circle cx="245" cy="200" r="70" fill="url(#photoToneB)" role="img" aria-label="Photo: hands typing on a laptop with glowing data charts"/>

    <!-- tagline -->
    <text class="tagline" x="418" y="63"><tspan class="accent">Connect data</tspan><tspan class="soft"> to</tspan></text>
    <text class="tagline" x="418" y="98"><tspan class="soft">increase</tspan> the flow of</text>
    <text class="tagline" x="418" y="133">profitability.</text>

    <!-- services frame -->
    <path d="M708 163 L378 163 Q368 163 368 173 L368 273 Q368 283 378 283 L735 283 Q745 283 745 273 L745 222"
          fill="none" stroke="var(--green)" stroke-width="4"/>
    <text class="services-title" x="404" y="197" fill="var(--ink)">2 primary services</text>
    <circle cx="409" cy="227" r="4" fill="var(--green)"/>
    <text class="service" x="421" y="232">Business Automation Services</text>
    <circle cx="409" cy="254" r="4" fill="var(--green)"/>
    <text class="service" x="421" y="259">AI (artificial intelligence integrations)</text>
  </svg>
</section>

</body>
</html>
```